Registration Page - Webinar

I need some proposition for a high conversion landing page for a Webinar.
This LP should follow some (minimal) rules:
1 - We need to have a registration box at it
2 - 1, 2 or 3 Keynote Speakers
3 - Featuring Time & Date
4 - All webinars will be free
5 - Title of the webinar
6 - Description of the webinar
7 - Should harmonize with my home page colors (www.themarbleharbor.com)

```html
<!DOCTYPE html>
<html lang="en">
<head>
<meta charset="utf-8">
<title>Free Webinar Registration – The Marble Harbor</title>
<link href="https://fonts.googleapis.com/css2?family=Poppins:wght@400;500;600;700&family=Roboto:wght@500&display=swap" rel="stylesheet">
<style>
:root{
  --pink:#e5106f;
  --orange:#f47a20;
  --teal:#1f9bbf;
  --teal-dark:#167f9f;
  --ink:#111;
  --navy:#2b2a5e;
  --green:#21b24b;
  --grey-line:#cfcfcf;
  --footer-bg:#f1f1f1;
  --footer-dark:#1f1f1f;
  --placeholder:#9a9a9a;
}
*{box-sizing:border-box;margin:0;padding:0}
html,body{width:1200px;height:2623px;overflow:hidden;background:#fff}
body{position:relative;font-family:'Poppins',sans-serif;color:var(--ink)}
.abs{position:absolute}

/* top navigation */
.topbar{left:89px;top:0;width:1024px;height:41px;background:var(--pink)}
.topbar nav{position:absolute;left:95px;top:11px;display:flex;gap:24px}
.topbar nav a{color:#fff;font-size:10px;font-weight:500;text-decoration:none}
.social{position:absolute;right:94px;top:14px;display:flex;gap:12px}
.social span{width:11px;height:11px;background:#fff;border-radius:2px;display:block}

.header{left:89px;top:41px;width:1024px;height:72px;background:#fff;box-shadow:0 3px 3px rgba(0,0,0,.18)}
.logo-bump{left:528px;top:80px;width:146px;height:60px;background:#fff;border-radius:0 0 73px 73px;box-shadow:0 3px 3px rgba(0,0,0,.18)}
.logo{left:500px;top:54px;width:200px;text-align:center;color:var(--pink);font-weight:700;font-size:22px;line-height:24px;letter-spacing:1px}
.logo small{display:block;font-size:12px;letter-spacing:4px;line-height:16px}
.wa{display:flex;align-items:center;gap:6px;background:var(--green);color:#fff;font-weight:600;border-radius:2px}
.wa-sm{left:236px;top:56px;height:21px;padding:0 7px;font-size:10px}
.phones{display:flex;gap:14px;font-size:10px;color:#333;align-items:center}
.phones span{display:flex;align-items:center;gap:3px}
.flag{width:14px;height:10px;display:inline-block;border-radius:1px}
.flag.br{background:var(--green)}
.flag.us{background:#c9354a}
.phones-sm{left:197px;top:85px}
.cta{display:flex;align-items:center;gap:8px;color:var(--navy);font-weight:600;font-size:10px;line-height:11px;text-transform:uppercase}
.cta i{width:32px;height:32px;border-radius:50%;display:flex;align-items:center;justify-content:center}
.cta i.p{background:var(--pink)} .cta i.t{background:var(--teal)}

/* hero */
.hero-photo{left:175px;top:202px;width:415px;height:319px;background:linear-gradient(160deg,#b9c6d4 0%,#9fb3c9 45%,#c9b8a3 75%,#d9764a 100%)}
.date{left:614px;top:201px;color:var(--pink);font-size:13px}
.hero-title{left:614px;top:218px;font-size:37px;font-weight:500;line-height:44px;width:430px}
.hero-copy{left:614px;top:314px;width:420px;font-size:13.4px;line-height:16.2px;color:#222}
.btn{background:var(--orange);color:#fff;font-family:'Roboto',sans-serif;font-weight:500;font-size:17px;display:flex;align-items:center;justify-content:center}
.btn-reg{left:614px;top:449px;width:220px;height:46px}

/* speakers */
.speakers{left:0;top:661px;width:1200px;height:734px;background:linear-gradient(120deg,var(--teal) 0%,#2aa3c6 55%,var(--teal-dark) 100%)}
.speakers .kicker{position:absolute;top:43px;width:100%;text-align:center;color:#fff;font-size:22px}
.speakers h2{position:absolute;top:84px;width:100%;text-align:center;color:#fff;font-size:37px;font-weight:500}
.portrait{position:absolute;left:248px;top:186px;width:218px;height:218px;background:linear-gradient(180deg,#8a6a55,#c48f78 55%,#b8222c)}
.sp-name{position:absolute;left:518px;top:179px;color:#fff;font-size:24px;font-weight:500;line-height:28px}
.sp-role{position:absolute;left:518px;top:207px;color:#fff;font-size:18px;line-height:21px;width:320px}
.sp-bio{position:absolute;left:517px;top:279px;width:440px;color:#fff;font-size:13.4px;line-height:16.3px}
.sp-bio p{margin-bottom:16px}
.arrow{position:absolute;top:382px}
.dots{position:absolute;top:620px;left:573px;display:flex;gap:9px}
.dots span{width:12px;height:12px;border-radius:50%;background:#fff}
.dots span:first-child{background:#166d88}

/* register */
.reg-title{left:247px;top:1514px;color:var(--pink);font-size:38px;font-weight:500;line-height:44px}
.field{left:247px;width:341px;height:37px;border:1px solid var(--grey-line);border-radius:3px;font-size:13.5px;color:var(--placeholder);padding:9px 16px}
.textarea{left:614px;top:1633px;width:416px;height:218px;border:1px solid var(--grey-line);border-radius:3px;font-size:13.5px;color:var(--placeholder);padding:11px 17px}
.collect-h{left:617px;top:1859px;color:var(--pink);font-size:13.5px;font-weight:500}
.collect{left:617px;top:1889px;width:416px;color:var(--pink);font-size:10.3px;line-height:12.5px}
.mandatory{left:617px;top:1977px;color:var(--pink);font-size:10px}
.btn-submit{left:561px;top:2042px;width:220px;height:45px}

/* footer */
.skyline{left:89px;top:2228px;width:1024px;height:80px;background:linear-gradient(180deg,#fff 0%,#e6e6e6 100%)}
.footer{left:89px;top:2308px;width:1024px;height:266px;background:var(--footer-bg)}
.loc{left:173px;width:290px;font-size:10px;line-height:17px;color:#333}
.loc b{display:flex;align-items:center;gap:6px;color:var(--navy);font-size:13.5px;font-weight:600;line-height:20px}
.f-logo{left:480px;top:2350px;width:240px;text-align:center;color:var(--pink);font-weight:700;font-size:33px;line-height:36px;letter-spacing:1px}
.f-logo small{display:block;font-size:18px;letter-spacing:6px;line-height:24px}
.wa-lg{left:789px;top:2327px;height:29px;padding:0 14px;font-size:15px}
.phones-lg{left:775px;top:2365px;font-size:11px}
.cta-lg{font-size:13px;line-height:16px}
.cta-lg i{width:32px;height:32px}
.bottombar{left:89px;top:2574px;width:1024px;height:49px;background:var(--footer-dark);color:#fff;font-size:8px;font-weight:600}
.bottombar .copy{position:absolute;left:84px;top:20px}
.bottombar .copy em{font-style:normal;color:var(--pink)}
.bottombar nav{position:absolute;right:84px;top:20px;display:flex;gap:30px}
.bottombar nav a{color:#fff;text-decoration:none}
.bottombar nav a.on{color:var(--pink)}
</style>
</head>
<body>

<div class="abs topbar">
  <nav><a>HOME</a><a>ABOUT US</a><a>PORTFOLIO</a><a>PROPERTIES</a><a>NEWS</a><a>EBOOKS</a><a>CONTACT</a></nav>
  <div class="social"><span></span><span></span><span></span></div>
</div>
<div class="abs header"></div>
<div class="abs logo-bump"></div>
<div class="abs logo">MARBLE<small>HARBOR</small></div>

<div class="abs wa wa-sm">
  <svg width="11" height="11" viewBox="0 0 24 24"><path fill="#fff" d="M6.6 10.8a15 15 0 0 0 6.6 6.6l2.2-2.2c.3-.3.7-.4 1-.2 1.1.4 2.3.6 3.6.6.6 0 1 .4 1 1V20c0 .6-.4 1-1 1A17 17 0 0 1 3 4c0-.6.4-1 1-1h3.5c.6 0 1 .4 1 1 0 1.3.2 2.5.6 3.6.1.3 0 .7-.2 1z"/></svg>
  US + (555) 210-4400
</div>
<div class="abs phones phones-sm"><span><i class="flag br"></i>+55 21 5550-1200</span><span><i class="flag us"></i>+1 (555) 300-7788</span></div>

<div class="abs cta" style="left:759px;top:63px">
  <i class="p"><svg width="16" height="16" viewBox="0 0 24 24" fill="none" stroke="#fff" stroke-width="2"><path d="M4 5h16v10H9l-5 4z"/></svg></i>Talk to an<br>agent
</div>
<div class="abs cta" style="left:894px;top:63px">
  <i class="t"><svg width="16" height="16" viewBox="0 0 24 24" fill="none" stroke="#fff" stroke-width="2"><rect x="4" y="5" width="16" height="15"/><path d="M4 10h16M8 3v4M16 3v4"/></svg></i>Schedule a<br>conversation
</div>

<!-- hero -->
<div class="abs hero-photo" role="img" aria-label="Photo of a person signing papers beside a small model house and keys"></div>
<div class="abs date">FREE WEBINAR : Sunday, April 5th 2020</div>
<h1 class="abs hero-title">What does COVID-19 mean for real estate?</h1>
<p class="abs hero-copy">As the COVID-19 pandemic dominates headlines and continues to cause global disruption at an unprecedented level, the predicted impact on the Australian economy changes daily. Around the world, financial markets, businesses and the social rhythms of daily life have been turned upside down, and at Northcove Group we remain committed to keeping our customers informed.</p>
<div class="abs btn btn-reg">FREE REGISTRATION</div>

<!-- speakers -->
<section class="abs speakers" role="img" aria-label="Teal-tinted photo of an audience seated in a seminar room">
  <div class="kicker">Webinar Keynote Speakers</div>
  <h2>What does COVID-19 mean for real estate?</h2>
  <div class="portrait" role="img" aria-label="Portrait photo of the keynote speaker"></div>
  <div class="sp-name">Jordan Ellery</div>
  <div class="sp-role">Executive Manager of Economic Research - Northcove Group</div>
  <div class="sp-bio">
    <p>Jordan is the Executive Manager of Economic Research at Northcove Group. He has worked in several areas of the property sector throughout his career and has more than 15 years' experience working as a property market analyst in both the residential and commercial fields.</p>
    <p>Jordan's experience spans valuations, property development, development consulting, commercial property research as well as residential property research. Through his work, Jordan has gained a thorough understanding of property market fundamentals across demographics, trends and economics, making him a widely sought-after commentator and presenter on property market conditions and emerging trends.</p>
    <p>Prior to joining Northcove Group, Jordan spent more than 11 years at Atlas Data where he was the Head of Research for Australia.</p>
  </div>
  <svg class="arrow" style="left:174px" width="18" height="28" viewBox="0 0 18 28"><path d="M15 3 4 14l11 11" fill="none" stroke="#fff" stroke-width="4"/></svg>
  <svg class="arrow" style="left:1010px" width="18" height="28" viewBox="0 0 18 28"><path d="M3 3l11 11L3 25" fill="none" stroke="#fff" stroke-width="4"/></svg>
  <div class="dots"><span></span><span></span><span></span></div>
</section>

<!-- registration -->
<h2 class="abs reg-title">Register Now<br>For FREE Webinar</h2>
<div class="abs field" style="top:1633px">First Name*</div>
<div class="abs field" style="top:1680px">Surname*</div>
<div class="abs field" style="top:1725px">Agency Name*</div>
<div class="abs field" style="top:1770px">Agency ID</div>
<div class="abs field" style="top:1818px">State*</div>
<div class="abs field" style="top:1864px">Phone Number</div>
<div class="abs field" style="top:1907px">Email*</div>
<div class="abs textarea">Questions for keynote speaker</div>
<div class="abs collect-h">Collection Statement</div>
<p class="abs collect">We will collect and use your personal information to help you and your office participate in the webinar. We may also use your email to obtain feedback and promote the services and products of harborhomes.com.au and third parties. Our Privacy Policy further explains how we collect, use and disclose personal information and how to access, correct and complain about the handling of personal information</p>
<div class="abs mandatory">* Mandatory Fields</div>
<div class="abs btn btn-submit">SUBMIT</div>

<!-- footer -->
<div class="abs skyline" role="img" aria-label="Faint grey city skyline silhouette"></div>
<div class="abs footer"></div>

<div class="abs loc" style="top:2330px"><b><svg width="9" height="12" viewBox="0 0 12 16"><path fill="#e5106f" d="M6 0a6 6 0 0 0-6 6c0 4.5 6 10 6 10s6-5.5 6-10a6 6 0 0 0-6-6zm0 8.5A2.5 2.5 0 1 1 6 3.5a2.5 2.5 0 0 1 0 5z"/></svg>Coastline Studio Barra</b>2nd Floor, Av. Litorânea 1200,<br>Barra Sul - RJ - Brazil</div>
<div class="abs loc" style="top:2399px"><b><svg width="9" height="12" viewBox="0 0 12 16"><path fill="#e5106f" d="M6 0a6 6 0 0 0-6 6c0 4.5 6 10 6 10s6-5.5 6-10a6 6 0 0 0-6-6zm0 8.5A2.5 2.5 0 1 1 6 3.5a2.5 2.5 0 0 1 0 5z"/></svg>Parque Norte Mall</b>Rua das Palmeiras, 480 Sala 12, Vila Alta<br>- São Paulo - Brazil</div>
<div class="abs loc" style="top:2467px;width:300px"><b><svg width="9" height="12" viewBox="0 0 12 16"><path fill="#e5106f" d="M6 0a6 6 0 0 0-6 6c0 4.5 6 10 6 10s6-5.5 6-10a6 6 0 0 0-6-6zm0 8.5A2.5 2.5 0 1 1 6 3.5a2.5 2.5 0 0 1 0 5z"/></svg>Orlando</b>1420 Lakeview Avenue, Suite 210, Orlando, USA</div>
<div class="abs loc" style="top:2514px;width:300px"><b><svg width="14" height="10" viewBox="0 0 16 12"><rect width="16" height="12" fill="#e5106f"/><path d="M0 0l8 6 8-6" fill="none" stroke="#fff" stroke-width="1.5"/></svg>Contact@Themarbleharbor.Com</b></div>

<div class="abs f-logo">MARBLE<small>HARBOR</small></div>

<div class="abs wa wa-lg">
  <svg width="15" height="15" viewBox="0 0 24 24"><path fill="#fff" d="M6.6 10.8a15 15 0 0 0 6.6 6.6l2.2-2.2c.3-.3.7-.4 1-.2 1.1.4 2.3.6 3.6.6.6 0 1 .4 1 1V20c0 .6-.4 1-1 1A17 17 0 0 1 3 4c0-.6.4-1 1-1h3.5c.6 0 1 .4 1 1 0 1.3.2 2.5.6 3.6.1.3 0 .7-.2 1z"/></svg>
  US + (555) 210-4400
</div>
<div class="abs phones phones-lg"><span><i class="flag br"></i>+55 21 5550-1200</span><span><i class="flag us"></i>+1 (555) 300-7788</span></div>
<div class="abs cta cta-lg" style="left:760px;top:2409px">
  <i class="p"><svg width="16" height="16" viewBox="0 0 24 24" fill="none" stroke="#fff" stroke-width="2"><path d="M4 5h16v10H9l-5 4z"/></svg></i>Talk to an<br>agent
</div>
<div class="abs cta cta-lg" style="left:894px;top:2409px">
  <i class="t"><svg width="16" height="16" viewBox="0 0 24 24" fill="none" stroke="#fff" stroke-width="2"><rect x="4" y="5" width="16" height="15"/><path d="M4 10h16M8 3v4M16 3v4"/></svg></i>Schedule a<br>conversation
</div>

<div class="abs bottombar">
  <div class="copy">© 2017 - THE MARBLE HARBOR BY <em>NOVAWEB</em></div>
  <nav><a class="on">HOME</a><a>PROPERTIES</a><a>NEWS</a><a>CONTACT</a><a>TERMS OF USE</a></nav>
</div>

</body>
</html>
```